Logo for KEX Co. roofing company
KEX, Co.
Professional
Dalmon Fitch
Owner
17 Hollet Lane Tamsford, KX 02974
Estimates
kexcoroofing@brightpost.net
kexcoroofing.net
Fully Insured
I want long used as the focus point. Company colors: Primary- Green, secondary- Black and yellow. on the back of the card I want kexcoroofing.net to be centered
brambeek brambeek
Please upload your logo Ai file.. thanks
Fitch42 Fitch42
I already have a logo that was previously made for me, I would like for that logo to be used.

```html
<!DOCTYPE html>
<html lang="en">
<head>
<meta charset="utf-8">
<title>KEX Co. Business Card</title>
<link href="https://fonts.googleapis.com/css2?family=Questrial&display=swap" rel="stylesheet">
<style>
  :root {
    --bg: #5f574b;
    --card: #161616;
    --green: #1f9a2c;
    --accent: #8fb31c;
    --white: #f1f1f1;
    --rule: #8a8a8a;
  }
  * { margin: 0; padding: 0; box-sizing: border-box; }
  html, body { width: 1200px; height: 904px; overflow: hidden; }
  body {
    background: var(--bg);
    font-family: "Questrial", "Century Gothic", sans-serif;
    position: relative;
  }
  .card {
    position: absolute;
    left: 250px;
    width: 700px;
    height: 400px;
    background: var(--card);
    box-shadow: 0 10px 28px rgba(0,0,0,.35);
    overflow: hidden;
  }
  .card--front { top: 32px; }
  .card--back { top: 472px; }

  .brand { color: var(--green); text-align: center; }
  .brand__name { font-size: 48px; letter-spacing: 2px; line-height: 1; }
  .brand__tagline { font-size: 10px; letter-spacing: 1.5px; margin-top: 6px; }

  .card--front .brand { position: absolute; top: 140px; left: 0; right: 0; }
  .front-url {
    position: absolute; top: 232px; left: 0; right: 0;
    text-align: center; color: var(--white); font-size: 17px;
  }
  .front-url span { color: var(--green); }

  .card--back .brand { position: absolute; top: 70px; left: 40px; text-align: left; }
  .card--back .brand__name { font-size: 40px; }
  .card--back .brand__tagline { font-size: 9px; }

  .owner { position: absolute; top: 74px; right: 40px; text-align: right; }
  .owner__name { color: var(--green); font-size: 20px; }
  .owner__title { color: var(--white); font-size: 12px; margin-top: 4px; }
  .owner-rule {
    position: absolute; top: 124px; left: 420px; right: 0;
    height: 1px; background: var(--rule);
  }

  .address-rule {
    position: absolute; top: 264px; left: 40px; width: 262px;
    height: 1px; background: var(--rule);
  }
  .address {
    position: absolute; top: 300px; left: 40px;
    color: var(--white); font-size: 14px; line-height: 1.35;
  }
  .divider {
    position: absolute; top: 266px; left: 306px; width: 1px; height: 96px;
    background: var(--rule);
  }
  .contacts {
    position: absolute; top: 266px; left: 316px;
    list-style: none; color: var(--white); font-size: 13px;
  }
  .contacts li { display: flex; align-items: center; height: 18px; }
  .contacts svg { width: 11px; height: 11px; margin-right: 10px; flex: none; }
  .band {
    position: absolute; left: 0; right: 0; bottom: 0; height: 14px;
    background: var(--accent);
  }
</style>
</head>
<body>

<section class="card card--front">
  <div class="brand">
    <div class="brand__name">KEX Co.</div>
    <div class="brand__tagline">ROOFING · SIDING · CARPENTRY · COPPER</div>
  </div>
  <p class="front-url">www.<span>kexcoroofing</span>.net</p>
</section>

<section class="card card--back">
  <div class="brand">
    <div class="brand__name">KEX Co.</div>
    <div class="brand__tagline">ROOFING · SIDING · CARPENTRY · COPPER</div>
  </div>

  <div class="owner">
    <div class="owner__name">Dalmon Fitch</div>
    <div class="owner__title">Owner</div>
  </div>
  <div class="owner-rule"></div>

  <div class="address-rule"></div>
  <p class="address">17 Hollet Lane<br>Tamsford, KX 02974</p>

  <div class="divider"></div>
  <ul class="contacts">
    <li><svg viewBox="0 0 12 12"><path d="M3 1h2l1 3-1.5 1a6 6 0 0 0 2.5 2.5L8 6l3 1v2a2 2 0 0 1-2 2A8 8 0 0 1 1 3a2 2 0 0 1 2-2z" fill="var(--green)"/></svg>617-555-0142</li>
    <li><svg viewBox="0 0 12 12"><path d="M3 1h2l1 3-1.5 1a6 6 0 0 0 2.5 2.5L8 6l3 1v2a2 2 0 0 1-2 2A8 8 0 0 1 1 3a2 2 0 0 1 2-2z" fill="var(--green)"/></svg>617-555-0187</li>
    <li><svg viewBox="0 0 12 12"><path d="M3 1h2l1 3-1.5 1a6 6 0 0 0 2.5 2.5L8 6l3 1v2a2 2 0 0 1-2 2A8 8 0 0 1 1 3a2 2 0 0 1 2-2z" fill="var(--green)"/></svg>781-555-0126</li>
    <li><svg viewBox="0 0 12 12"><rect x="1" y="2.5" width="10" height="7" rx="1" fill="var(--green)"/><path d="M1.5 3l4.5 3.5L10.5 3" stroke="var(--card)" fill="none"/></svg>kexcoroofing@brightpost.net</li>
    <li><svg viewBox="0 0 12 12"><circle cx="6" cy="6" r="5" fill="var(--green)"/><path d="M1 6h10M6 1c-2 3-2 7 0 10M6 1c2 3 2 7 0 10" stroke="var(--card)" stroke-width=".8" fill="none"/></svg>www.kexcoroofing.net</li>
  </ul>

  <div class="band"></div>
</section>

</body>
</html>
```